Webpage

I am a professional genealogist. I need a webpage that is professional looking (using the logo I chose), I can add hyperlinks and photos to if and when I want.

```html
<!DOCTYPE html>
<html lang="en">
<head>
<meta charset="utf-8">
<title>Lineage Research Services</title>
<link href="https://fonts.googleapis.com/css2?family=Merriweather:wght@400&family=Playfair+Display:wght@400;700&family=Ubuntu:wght@300;400;500&display=swap" rel="stylesheet">
<style>
:root{
  --ink:#333;
  --muted:#8a8a8a;
  --topbar:#2b2b2b;
  --teal:#14a8c2;
  --blue:#5aa6df;
  --green:#3db879;
  --panel:#f5f5f5;
  --line:#cfcfcf;
  --footer:#2f2f2f;
  --footer-low:#3b3b3b;
  --white:#fff;
}
*{box-sizing:border-box;margin:0;padding:0}
html,body{width:1200px;height:2596px;overflow:hidden}
body{position:relative;background:var(--white);font-family:'Ubuntu',sans-serif;color:var(--ink)}
.abs{position:absolute}
.serif{font-family:'Playfair Display',serif}

.topbar{left:0;top:0;width:1200px;height:28px;background:var(--topbar);color:#ddd;font-size:12px}
.topbar .contact{left:32px;top:7px;display:flex;gap:30px;align-items:center}
.topbar .contact span{display:flex;gap:8px;align-items:center}
.topbar .social{right:30px;top:9px;display:flex;gap:20px}
.topbar .social i{display:block;width:10px;height:10px;background:#777;border-radius:2px}

.header{left:0;top:28px;width:1200px;height:86px;background:var(--white)}
.brand{left:140px;top:24px;display:flex;align-items:center;gap:10px;font-size:17px;font-weight:500;color:#2a4d5a}
.brand i{width:36px;height:36px;border-radius:50%;background:var(--teal);display:block}
.nav{top:32px;left:0;width:1200px;font-size:16px}
.nav a{position:absolute;color:var(--ink);text-decoration:none}
.nav a.active::after{content:"";position:absolute;left:-6px;right:-6px;top:44px;height:4px;background:var(--blue)}

.hero{left:0;top:114px;width:1200px;height:452px;background:linear-gradient(90deg,#1c1c1c 0%,#3a3835 45%,#6b625a 62%,#2a2826 100%)}
.hero h1{left:178px;top:112px;color:var(--white);font-family:'Merriweather','Playfair Display',serif;font-weight:400;font-size:34px}
.hero p{left:182px;top:160px;width:360px;color:#eee;font-size:17px;line-height:24px;text-align:justify}
.btn-blue{left:352px;top:250px;width:136px;height:38px;background:var(--blue);color:var(--white);font-family:'Playfair Display',serif;font-size:16px;display:flex;align-items:center;justify-content:center;border:1px solid #8cc4ee}
.searchbar{left:150px;top:364px;width:900px;height:88px;background:rgba(255,255,255,.82)}
.searchbar .field{left:36px;top:18px;width:276px;height:48px;border:2px solid #a9dccb;background:var(--white);color:#999;font-size:16px;display:flex;align-items:center;justify-content:center}
.searchbar .go,.searchbar .calc{top:18px;width:84px;height:48px;background:var(--teal);display:flex;align-items:center;justify-content:center}
.searchbar .go{left:328px}
.searchbar .calc{left:754px;width:118px}
.searchbar .est{left:560px;top:26px;font-size:24px;color:#333}

.service{top:616px;width:232px}
.service .icon{left:0;top:0;width:70px;height:70px;background:#e6eef1;border:1px solid #9bb}
.service h3{left:96px;top:6px;font-family:'Playfair Display',serif;font-weight:400;font-size:19px;line-height:24px;color:#333}
.service p{left:4px;top:82px;width:226px;font-size:13px;line-height:18px;color:#777}
.btn-green{left:2px;top:172px;width:114px;height:32px;background:var(--green);color:var(--white);font-family:'Playfair Display',serif;font-size:15px;display:flex;align-items:center;justify-content:center}

.infobox{left:132px;top:876px;width:936px;height:436px;background:var(--panel);border:2px solid var(--line)}
.infobox .divider{left:556px;top:0;width:2px;height:432px;background:var(--line)}
.infobox h2{font-family:'Playfair Display',serif;font-weight:400;font-size:22px;color:#333}
.about-photo{left:16px;top:62px;width:234px;height:164px;border:2px solid #ccc;background:var(--white);padding:8px}
.about-photo div{width:100%;height:100%;background:linear-gradient(180deg,#b9b4ae,#5b5650)}
.about-text{font-size:14px;line-height:20px;color:#888;text-align:justify}
.readmore{color:var(--blue);font-size:15px;display:flex;gap:6px;align-items:center}
.news{left:564px;width:370px;height:150px}
.news .date{left:0;top:0;width:58px;height:78px}
.news .date b{display:flex;height:42px;background:var(--teal);color:var(--white);font-family:'Playfair Display',serif;font-weight:400;font-size:24px;align-items:center;justify-content:center}
.news .date span{display:flex;height:36px;background:#2f2f2f;color:var(--white);font-size:14px;align-items:center;justify-content:center}
.news h4{left:72px;top:8px;font-family:'Playfair Display',serif;font-weight:400;font-size:18px}
.news .meta{left:76px;top:36px;font-size:13px;color:var(--teal);font-style:italic;display:flex;gap:26px}
.news p{left:80px;top:70px;width:280px;font-size:14px;line-height:20px;color:#888}

.projects h2{left:132px;top:1366px;font-family:'Playfair Display',serif;font-weight:400;font-size:22px}
.arrows{left:1036px;top:1384px;display:flex;gap:2px}
.arrows i{display:flex;width:15px;height:15px;background:#333;align-items:center;justify-content:center}
.project{top:1412px;width:218px;height:138px}

.band{left:0;top:1606px;width:1200px;height:438px;background:var(--teal);color:var(--white)}
.band h2{font-family:'Playfair Display',serif;font-weight:400;font-size:22px}
.tweet .avatar{left:140px;top:80px;width:62px;height:60px;background:var(--white);padding:4px}
.tweet .avatar div{width:100%;height:100%;background:#a9d8c9}
.tweet .body{left:216px;top:96px;width:450px;font-size:12px;line-height:17px}
.tweet .body p{margin-bottom:12px}
.dots{left:336px;top:288px;display:flex;gap:11px}
.dots i{width:10px;height:10px;border-radius:50%;background:#222;display:block}
.dots i:first-child{background:var(--white)}
.quote{left:700px;top:80px;width:358px;height:190px;background:var(--white);color:#777;font-size:14px;line-height:20px;padding:26px 22px 0 44px}
.quote p{margin-bottom:10px}
.quote .mark{position:absolute;left:16px;top:18px}
.person .face{left:700px;top:304px;width:50px;height:52px;background:linear-gradient(#d8d4cf,#6e6a66)}

.footer{left:0;top:2044px;width:1200px;height:476px;background:var(--footer);color:#ccc}
.footer h3{font-family:'Playfair Display',serif;font-weight:400;font-size:17px;color:var(--white);padding-bottom:10px;border-bottom:1px solid #555;width:280px}
.footer .intro{left:130px;top:76px;width:256px;font-size:12px;line-height:18px;color:#777}
.footer .item{left:130px;display:flex;gap:14px;font-size:12px;line-height:22px;color:#ddd}
.posts{left:450px;top:78px;width:280px}
.posts li{list-style:none;font-size:12px;color:#eee;height:48px;border-bottom:1px solid #474747;display:flex;align-items:center;gap:10px}
.form label{display:block;font-size:12px;color:#eee}
.form .in{background:#3d3d3d;border:1px solid #555}
.submit{background:#1e1e1e;color:var(--white);font-size:14px;display:flex;align-items:center;justify-content:center}

.bottom{left:0;top:2520px;width:1200px;height:76px;background:var(--footer-low)}
.bottom .copy{left:130px;top:30px;font-size:11px;color:#ddd}
.bottom .social{left:768px;top:24px;display:flex;gap:8px}
.bottom .social i{display:block;width:30px;height:30px;border:1px solid #888}
</style>
</head>
<body>

<div class="abs topbar">
  <div class="abs contact">
    <span><svg width="8" height="13" viewBox="0 0 8 13"><rect x="0.5" y="0.5" width="7" height="12" rx="1" fill="none" stroke="#ddd"/><circle cx="4" cy="10.5" r="0.8" fill="#ddd"/></svg>Call us : 512-555-0148</span>
    <span><svg width="13" height="9" viewBox="0 0 13 9"><rect width="13" height="9" fill="#ddd"/><path d="M0 0l6.5 5L13 0" fill="none" stroke="#2b2b2b"/></svg>email: info@lineageresearch.example</span>
  </div>
  <div class="abs social"><i></i><i></i><i></i><i></i></div>
</div>

<header class="abs header">
  <div class="abs brand"><i></i>Lineage Research Services</div>
  <nav class="abs nav">
    <a class="active" style="left:452px">Home</a>
    <a style="left:536px">About</a>
    <a style="left:614px">Services</a>
    <a style="left:690px">Publications</a>
    <a style="left:796px">Blog</a>
    <a style="left:878px">Links</a>
    <a style="left:954px">Contact</a>
  </nav>
</header>

<section class="abs hero" role="img" aria-label="Portrait of a smiling woman over faded family photographs">
  <h1 class="abs">Lorem ipsum dolor</h1>
  <p class="abs">Excepteur sint occaecat cupidatat non proident, sunt in culpa qui officia deserunt.</p>
  <div class="abs btn-blue">Read More</div>
  <div class="abs searchbar">
    <div class="abs field">Search in this site</div>
    <div class="abs go"><svg width="34" height="34" viewBox="0 0 34 34"><circle cx="14" cy="14" r="10" fill="none" stroke="#fff" stroke-width="3"/><path d="M21 21l10 10" stroke="#fff" stroke-width="4"/></svg></div>
    <div class="abs est serif">Get an Estimate</div>
    <div class="abs calc"><svg width="32" height="32" viewBox="0 0 32 32" fill="none" stroke="#fff" stroke-width="2"><rect x="2" y="2" width="28" height="28"/><path d="M16 2v28M2 16h28M6 9h6M9 6v6M20 9h6M6 23h6M20 21h6M20 25h6"/></svg></div>
  </div>
</section>

<section>
  <div class="abs service" style="left:130px">
    <div class="abs icon" role="img" aria-label="Icon of a person with a magnifying glass"></div>
    <h3 class="abs">Forensic<br>Genealogy</h3>
    <p class="abs">Lorem ipsum dolor sit amet, consectetur adipisicing elit, sed do eiusmod tempor incididunt ut labore et dolore magna aliqua.</p>
    <div class="abs btn-green">Read More</div>
  </div>
  <div class="abs service" style="left:370px">
    <div class="abs icon" role="img" aria-label="Icon of two people with a check mark"></div>
    <h3 class="abs">Kinship<br>Determination</h3>
    <p class="abs">Lorem ipsum dolor sit amet, consectetur adipisicing elit, sed do eiusmod tempor incididunt ut labore et dolore magna aliqua.</p>
    <div class="abs btn-green">Read More</div>
  </div>
  <div class="abs service" style="left:610px">
    <div class="abs icon" role="img" aria-label="Icon of a DNA strand and microscope"></div>
    <h3 class="abs">Research<br>Analysis &amp;<br>Consultation</h3>
    <p class="abs">Lorem ipsum dolor sit amet, consectetur adipisicing elit, sed do eiusmod tempor incididunt ut labore et dolore magna aliqua.</p>
    <div class="abs btn-green">Read More</div>
  </div>
  <div class="abs service" style="left:848px">
    <div class="abs icon" role="img" aria-label="Icon of a document with a refresh arrow"></div>
    <h3 class="abs">Record<br>Retrieval</h3>
    <p class="abs">Lorem ipsum dolor sit amet, consectetur adipisicing elit, sed do eiusmod tempor incididunt ut labore et dolore magna aliqua.</p>
    <div class="abs btn-green">Read More</div>
  </div>
</section>

<section class="abs infobox">
  <div class="abs divider"></div>
  <h2 class="abs" style="left:16px;top:14px">About Us</h2>
  <div class="abs about-photo"><div role="img" aria-label="Family group photograph"></div></div>
  <p class="abs about-text" style="left:266px;top:98px;width:250px">Sed ut perspiciatis unde omnis iste natus error sit voluptatem accusantium doloremque laudantium, totam rem aperiam, eaque ipsa quae ab illo inventore veritatis et quasi architecto beatae vitae dicta sunt explicabo.</p>
  <p class="abs about-text" style="left:16px;top:244px;width:504px">Neque porro quisquam est, qui dolorem ipsum quia dolor sit amet, consectetur, adipisci velit, sed quia non numquam eius modi tempora incidunt ut labore et dolore magnam aliquam quaerat voluptatem. Ut enim ad minima veniam, quis nostrum exercitationem ullam corporis suscipit laboriosam, nisi ut aliquid ex ea commodi consequatur.</p>
  <div class="abs readmore" style="left:362px;top:356px">Read More <svg width="9" height="16" viewBox="0 0 9 16"><path d="M1 1l7 7-7 7" fill="none" stroke="#5aa6df" stroke-width="2"/></svg></div>

  <h2 class="abs" style="left:566px;top:4px">Latest News</h2>
  <div class="abs news" style="top:48px">
    <div class="abs date"><b>20</b><span>May</span></div>
    <h4 class="abs">Lorem Ipsum</h4>
    <div class="abs meta"><span>&#9679; lineageresearch</span><span>&#9675; 10</span></div>
    <p class="abs">Lorem ipsum dolor sit amet, consectetur adipisicing elit, sed do eiusmod tempor incididunt ut labore et dolore magna aliqua. Ut enim ad minim [...]</p>
  </div>
  <div class="abs news" style="top:238px">
    <div class="abs date"><b>25</b><span>May</span></div>
    <h4 class="abs">Lorem Ipsum</h4>
    <div class="abs meta"><span>&#9679; lineageresearch</span><span>&#9675; 10</span></div>
    <p class="abs">Lorem ipsum dolor sit amet, consectetur adipisicing elit, sed do eiusmod tempor incididunt ut labore et dolore magna aliqua. Ut enim ad minim [...]</p>
  </div>
</section>

<section class="projects">
  <h2 class="abs">Our Projects</h2>
  <div class="abs arrows">
    <i><svg width="6" height="8"><path d="M5 0L1 4l4 4" fill="none" stroke="#fff"/></svg></i>
    <i><svg width="6" height="8"><path d="M1 0l4 4-4 4" fill="none" stroke="#fff"/></svg></i>
  </div>
  <div class="abs project" style="left:132px;background:linear-gradient(#8a8176,#3e3832)" role="img" aria-label="Vintage photo of a family with a soldier"></div>
  <div class="abs project" style="left:370px;background:linear-gradient(#a08c74,#4c3c2c)" role="img" aria-label="Sepia family portrait"></div>
  <div class="abs project" style="left:610px;background:linear-gradient(#5c5c5c,#151515)" role="img" aria-label="Black and white portrait of an elderly man"></div>
  <div class="abs project" style="left:852px;background:linear-gradient(#9a9792,#2e2c2a)" role="img" aria-label="Large family group photo outdoors"></div>
</section>

<section class="abs band">
  <h2 class="abs" style="left:146px;top:34px;display:flex;gap:10px;align-items:center"><svg width="18" height="15" viewBox="0 0 18 15"><rect width="18" height="15" rx="3" fill="#fff"/></svg>Latest Tweets</h2>
  <div class="tweet">
    <div class="abs avatar"><div role="img" aria-label="Profile picture"></div></div>
    <div class="abs" style="left:216px;top:76px;font-size:13px">@lineageresearch</div>
    <div class="abs body">
      <p>Nuevo post en mi blog, "Enigma del amor" Para aquellos a los que les guste divagar - See more at: http://samplenewsfeed.example/news-ticker/#sthash.aB3kQ7.dpuf</p>
      <p>http://t.co/xY7mQ2pL #enigma #amor #familia #blog - See more at: http://samplenewsfeed.example/news-ticker/#sthash.aB3kQ7.dpuf</p>
      <p style="margin-bottom:4px">2mins ago</p>
      <p style="display:flex;gap:22px">&#8630; Reply<span>&#8644; Retweet</span><span>&#9733; Favourite</span></p>
    </div>
  </div>
  <div class="abs dots"><i></i><i></i><i></i><i></i><i></i><i></i></div>

  <h2 class="abs" style="left:766px;top:44px">Testimonials</h2>
  <div class="abs quote">
    <svg class="mark" width="18" height="14" viewBox="0 0 18 14"><path d="M0 14V8C0 3 3 0 7 0v3C5 3 4 5 4 7h3v7zM11 14V8c0-5 3-8 7-8v3c-2 0-3 2-3 4h3v7z" fill="#14a8c2"/></svg>
    <p>Lorem ipsum dolor sit amet, consectetur adipisicing elit, sed do eiusmod tempor incididunt ut labore et dolore magna aliqua. Ut enim ad minim veniam, quis nostrud.</p>
    <p>Excepteur sint occaecat cupidatat non proident, sunt in culpa qui officia.</p>
  </div>
  <svg class="abs" style="left:716px;top:268px" width="28" height="30" viewBox="0 0 28 30"><path d="M0 0h28L0 30z" fill="#fff"/></svg>
  <div class="person">
    <div class="abs face" role="img" aria-label="Portrait of the client"></div>
    <div class="abs serif" style="left:770px;top:304px;font-size:17px;color:#222">Marcus Hale</div>
    <div class="abs" style="left:770px;top:332px;font-size:12px">Company</div>
  </div>
</section>

<footer class="abs footer">
  <h3 class="abs" style="left:130px;top:26px;border:none">Lineage Research Services</h3>
  <p class="abs intro">Sed ut perspiciatis unde omnis iste natus error sit voluptatem accusantium doloremque laudantium, totam rem aperiam, eaque ipsa quae ab illo inventore veritatis et quasi architecto</p>
  <div class="abs item" style="top:184px"><svg width="12" height="16" viewBox="0 0 12 16"><path d="M6 16S0 9 0 6a6 6 0 0112 0c0 3-6 10-6 10z" fill="#ddd"/><circle cx="6" cy="6" r="2" fill="#2f2f2f"/></svg><span>Dana Lindqvist, Professional Genealogist<br>PO Box 4410<br>Riverton, TX 78700-4410</span></div>
  <div class="abs item" style="top:286px"><svg width="10" height="16" viewBox="0 0 8 13"><rect x="0.5" y="0.5" width="7" height="12" rx="1" fill="none" stroke="#ddd"/></svg><span>512-555-0148</span></div>
  <div class="abs item" style="top:340px"><svg width="14" height="16" viewBox="0 0 13 9"><rect x="0.5" y="0.5" width="12" height="8" fill="none" stroke="#ddd"/><path d="M0 0l6.5 5L13 0" fill="none" stroke="#ddd"/></svg><span>dana@lineageresearch.example</span></div>

  <h3 class="abs" style="left:450px;top:26px">Recent Posts</h3>
  <ul class="abs posts">
    <li>&rsaquo; Lorem ipsum dolor sit amet, consectetur</li>
    <li>&rsaquo; Lorem ipsum dolor sit amet, consectetur</li>
    <li>&rsaquo; Lorem ipsum dolor sit amet, consectetur</li>
    <li>&rsaquo; Lorem ipsum dolor sit amet, consectetur</li>
    <li>&rsaquo; Lorem ipsum dolor sit amet, consectetur</li>
    <li>&rsaquo; Lorem ipsum dolor sit amet, consectetur</li>
    <li>&rsaquo; Lorem ipsum dolor sit amet, consectetur</li>
  </ul>

  <h3 class="abs" style="left:766px;top:26px">Contact</h3>
  <div class="form">
    <label class="abs" style="left:768px;top:86px">Enter Name :</label>
    <div class="abs in" style="left:766px;top:112px;width:302px;height:32px"></div>
    <label class="abs" style="left:768px;top:164px">Enter Email :</label>
    <div class="abs in" style="left:766px;top:190px;width:302px;height:32px"></div>
    <label class="abs" style="left:768px;top:246px">Your Query :</label>
    <div class="abs in" style="left:766px;top:272px;width:302px;height:108px"></div>
    <div class="abs submit" style="left:766px;top:402px;width:114px;height:44px">Submit</div>
  </div>
</footer>

<div class="abs bottom">
  <div class="abs copy">&copy; Lineage Research Services</div>
  <div class="abs social"><i></i><i></i><i></i><i></i></div>
</div>

</body>
</html>
```